Mini-Banner für Rubriken
Hallo,
wir benötigen für unsere Seite www.quilmar.de neue und vorallem passende Banner für die Highlights (rechte Seite) innerhalb der Rubriken, wie z.B. All Inklusive, Wellness, Urlaub an der Küste u.s.w. Vielen Dank für die Vorschläge !

```html
<!DOCTYPE html>
<html lang="de">
<head>
<meta charset="utf-8">
<title>Mini-Banner Rubriken – quilmar stays</title>
<link rel="stylesheet" href="https://fonts.googleapis.com/css2?family=Lobster&display=swap">
<style>
  :root {
    --page: #ffffff;
    --navy: #27307f;
    --red: #b5121b;
    --magenta: #cf1f86;
    --gold: #b39454;
    --outline: #ffffff;
    --sea-deep: #3fb5c6;
    --sea: #7fd0da;
    --sea-light: #bfe6ec;
    --foam: #f4f7f5;
    --sky: #2466bd;
    --sky-light: #9cc4ea;
    --cloud: #eef3f8;
    --beach: #d8cdbb;
    --beach-dark: #b9ad99;
    --petal: #f6f3ee;
    --lilac: #b7bfe4;
    --water: #7b7a62;
    --skin: #eab49a;
    --skin-light: #f3cdb2;
    --forest-dark: #1f4d1d;
    --forest: #2f6b2c;
    --forest-light: #5aa54b;
    --star: #f5a81c;
    --star-light: #ffd65a;
    --wood: #5a2a14;
    --wood-light: #8a4a24;
  }
  * { margin: 0; padding: 0; box-sizing: border-box; }
  html, body { width: 927px; height: 1200px; overflow: hidden; background: var(--page); }
  .sheet { position: relative; width: 927px; height: 1200px; }

  .banner {
    position: absolute; left: 60px; width: 798px;
    overflow: hidden;
    box-shadow: 0 3px 8px rgba(0,0,0,.35);
  }
  .banner__photo { position: absolute; inset: 0; }
  .banner__title {
    position: absolute;
    font-family: "Lobster", cursive;
    font-weight: 400;
    text-align: center;
    white-space: nowrap;
    letter-spacing: 1px;
    -webkit-text-stroke: 8px var(--outline);
    paint-order: stroke fill;
    text-shadow: 2px 3px 4px rgba(0,0,0,.35);
  }

  /* Küste */
  .banner--coast { top: 40px; height: 252px; }
  .banner--coast .banner__photo {
    background:
      radial-gradient(ellipse 60% 18% at 45% 60%, rgba(255,255,255,.9), rgba(255,255,255,0) 100%),
      radial-gradient(ellipse 50% 30% at 85% 20%, rgba(63,181,198,.6), rgba(63,181,198,0) 100%),
      linear-gradient(180deg, var(--sea-deep) 0%, var(--sea) 28%, var(--sea-light) 48%, var(--foam) 60%, var(--sea-light) 74%, #a8dbe6 100%);
  }
  .banner--coast .banner__title {
    left: 280px; width: 480px; top: 26px;
    font-size: 86px; line-height: 94px; color: var(--navy);
  }
  .decor-star {
    position: absolute; left: 30px; top: 20px; width: 180px; height: 174px;
    background: radial-gradient(circle at 50% 48%, var(--star-light) 0%, var(--star) 45%, rgba(245,168,28,0) 72%);
  }

  /* All-Inclusive */
  .banner--inclusive { top: 316px; height: 258px; }
  .banner--inclusive .banner__photo {
    background:
      radial-gradient(ellipse 30% 14% at 20% 12%, rgba(238,243,248,.85), rgba(238,243,248,0) 100%),
      radial-gradient(ellipse 34% 16% at 62% 18%, rgba(238,243,248,.85), rgba(238,243,248,0) 100%),
      radial-gradient(ellipse 26% 12% at 92% 22%, rgba(238,243,248,.75), rgba(238,243,248,0) 100%),
      radial-gradient(ellipse 70% 22% at 50% 72%, rgba(250,250,250,.7), rgba(250,250,250,0) 100%),
      linear-gradient(180deg, var(--sky) 0%, var(--sky-light) 36%, #cfe2ee 50%, var(--beach) 62%, var(--beach-dark) 100%);
  }
  .banner--inclusive .banner__title {
    left: 14px; right: 0; top: 64px;
    font-size: 100px; line-height: 110px; color: var(--red);
  }

  /* Wellness */
  .banner--wellness { top: 597px; height: 255px; }
  .banner--wellness .banner__photo {
    background:
      radial-gradient(ellipse 22% 30% at 32% 72%, rgba(255,255,255,.9), rgba(255,255,255,0) 100%),
      radial-gradient(ellipse 18% 20% at 30% 12%, rgba(255,255,255,.8), rgba(255,255,255,0) 100%),
      radial-gradient(ellipse 40% 50% at 80% 30%, var(--skin-light), rgba(243,205,178,0) 100%),
      linear-gradient(100deg, var(--lilac) 0%, #d9dcef 14%, var(--petal) 28%, #a7a38a 46%, var(--water) 55%, var(--skin) 78%, #d8a56a 100%);
  }
  .banner--wellness .banner__title {
    left: 334px; width: 440px; top: 42px; color: var(--magenta);
  }
  .banner--wellness .line-small { display: block; font-size: 64px; line-height: 66px; }
  .banner--wellness .line-big { display: block; font-size: 98px; line-height: 100px; }

  /* Harz */
  .banner--harz { top: 877px; height: 256px; }
  .banner--harz .banner__photo {
    background:
      radial-gradient(ellipse 30% 30% at 25% 30%, rgba(90,165,75,.7), rgba(90,165,75,0) 100%),
      radial-gradient(ellipse 35% 35% at 70% 70%, rgba(90,165,75,.6), rgba(90,165,75,0) 100%),
      radial-gradient(ellipse 30% 25% at 85% 15%, rgba(31,77,29,.6), rgba(31,77,29,0) 100%),
      linear-gradient(180deg, var(--forest) 0%, #3d8436 50%, var(--forest-dark) 100%);
  }
  .banner--harz .banner__title {
    left: 247px; width: 540px; top: 22px;
    font-size: 100px; line-height: 94px; color: var(--gold);
  }
  .decor-clock {
    position: absolute; left: 22px; top: 0; width: 212px; height: 252px;
    background: radial-gradient(ellipse 50% 50% at 50% 50%, var(--wood-light) 0%, var(--wood) 55%, rgba(90,42,20,0) 100%);
  }
</style>
</head>
<body>
<main class="sheet">
  <section class="banner banner--coast">
    <div class="banner__photo" role="img" aria-label="Foto: Meereswelle am Sandstrand"></div>
    <div class="decor-star" role="img" aria-label="Illustration: gelber Seestern"></div>
    <h2 class="banner__title">Urlaub an<br>der Küste</h2>
  </section>

  <section class="banner banner--inclusive">
    <div class="banner__photo" role="img" aria-label="Foto: gedeckte Tische und weiße Stühle am Strand unter blauem Himmel"></div>
    <h2 class="banner__title">All-Inclusive</h2>
  </section>

  <section class="banner banner--wellness">
    <div class="banner__photo" role="img" aria-label="Foto: Hand im Wasser mit Margeritenblüten und Teelichtern, bayerisches Rautenmuster"></div>
    <h2 class="banner__title"><span class="line-small">Wellnessurlaub</span><span class="line-big">in Bayern</span></h2>
  </section>

  <section class="banner banner--harz">
    <div class="banner__photo" role="img" aria-label="Foto: Nadelwald im Harz von oben"></div>
    <div class="decor-clock" role="img" aria-label="Illustration: geschnitzte Kuckucksuhr"></div>
    <h2 class="banner__title">Erholung im<br>Harz</h2>
  </section>
</main>
</body>
</html>
```